Corporate Powerpoint templates

I wish to have a standardized template for our manufacturing company. We manufacture baseball caps for major sport leagues and teams.
Our powerpoint should be clean, yet stylish.
We do a lot of presentations for technical trainings, KPI reports, quality assurance training.
We have factories in China, Bangladesh, and Mexico, so the look and feel must be internationally accepted.

Target Market(s)

Branded customers

Industry/Entity Type

Headwear Manufacturing

Font styles to use
Sans Serif

Colors
00AB8E
00BBA5
67D7C9
C6EFE9
E9F9F6

Requirements
Must have
• Spreadsheet slides, graphs, photographic reports
Nice to have
• Sporty, trendy, yet corporate feel.

```html
<!DOCTYPE html>
<html lang="en">
<head>
<meta charset="utf-8">
<title>Headwear Manufacturing – Corporate Presentation Template</title>
<link href="https://fonts.googleapis.com/css2?family=Playfair+Display:wght@800;900&family=Montserrat:wght@400;500;600;700&display=swap" rel="stylesheet">
<style>
  :root{
    --teal:#0fa98b;
    --teal-dark:#00957a;
    --gold:#d4bf98;
    --gold-dark:#c4aa78;
    --ink:#232323;
    --grey:#8a8a8a;
    --grey-card:#9b9c9e;
    --paper:#ffffff;
    --backdrop:#9a9a9b;
    --ring:#efefef;
  }
  *{box-sizing:border-box;margin:0;padding:0}
  html,body{width:1050px;height:1200px;overflow:hidden}
  body{background:linear-gradient(160deg,#a3a3a4,#8f8f90);font-family:"Montserrat",sans-serif;color:var(--ink);position:relative}
  .slide{position:absolute;width:320px;height:180px;background:var(--paper);overflow:hidden;box-shadow:2px 3px 6px rgba(0,0,0,.35)}
  .c1{left:35px}.c2{left:364px}.c3{left:693px}
  .r1{top:37px}.r2{top:228px}.r3{top:418px}.r4{top:607px}.r5{top:795px}.r6{top:984px}
  .abs{position:absolute}
  .teal{background:var(--teal)}
  .ttl{font-family:"Playfair Display",serif;font-weight:900;font-size:13px;line-height:1.05;color:var(--ink)}
  .ttl.white{color:#fff}
  .bars{position:absolute;left:0;width:16px;height:4px;border-top:.6px solid var(--gold);border-bottom:.6px solid var(--gold)}
  .bars::after{content:"";position:absolute;left:0;right:0;top:1.2px;border-top:.6px solid var(--gold)}
  .bd{font-size:3.4px;line-height:1.35;color:var(--grey)}
  .bd.white{color:#eafaf6}
  .hd{font-size:5.6px;font-weight:700;color:var(--ink)}
  .num{font-family:"Playfair Display",serif;font-weight:900;color:var(--gold);font-size:11px}
  .web{position:absolute;right:8px;bottom:6px;font-size:3.6px;letter-spacing:.6px;color:#444}
  .photo{position:absolute;background:linear-gradient(150deg,#3b4046,#1d2024 60%,#4a4f55)}
  .ring{position:absolute;border-radius:50%;border:5px solid var(--gold);background:#fff}
  .dots{position:absolute;display:grid;gap:2px}
  .dots i{display:block;width:1.4px;height:1.4px;border-radius:50%;background:var(--gold)}
  .icon{position:absolute;border-radius:50%;background:var(--gold);display:flex;align-items:center;justify-content:center}
  .center{text-align:center}
</style>
</head>
<body>

<!-- Row 1 -->
<section class="slide c1 r1">
  <div class="abs teal" style="left:220px;top:0;width:100px;height:180px"></div>
  <div class="abs" style="left:10px;top:19px;width:.6px;height:67px;background:var(--teal)"></div>
  <div class="abs" style="left:10px;top:103px;width:.6px;height:86px;background:var(--teal)"></div>
  <h1 class="ttl abs" style="left:18px;top:26px;font-size:14.5px;line-height:1.25;width:130px">Advice And<br>Counsel Throug<br>Email</h1>
  <div class="abs" style="left:141px;top:34px;font-size:8px;color:#444;letter-spacing:-1px">/////</div>
  <div class="photo" role="img" aria-label="Portrait of a player wearing a navy baseball cap" style="left:161px;top:20px;width:138px;height:138px"></div>
  <div class="ring" style="left:147px;top:144px;width:28px;height:28px"></div>
  <div class="abs" style="left:20px;top:108px;font-size:6.2px;font-weight:700;color:var(--teal)">We Manufacture</div>
  <div class="abs" style="left:20px;top:116px;font-size:6.2px;font-weight:600;line-height:1.4;width:120px">Baseball Caps For Major Sport Leagues And Teams</div>
  <div class="abs" style="left:20px;top:138px;width:24px;height:.6px;background:var(--gold)"></div>
  <div class="abs" style="left:20px;top:144px;font-size:4.6px;color:var(--teal)">Go to www.companywebsite.com</div>
  <div class="abs" style="left:268px;top:8px;display:flex;gap:7px">
    <span style="width:4.5px;height:4.5px;border-radius:50%;background:var(--gold)"></span><span style="width:4.5px;height:4.5px;border-radius:50%;background:var(--gold)"></span><span style="width:4.5px;height:4.5px;border-radius:50%;background:var(--gold)"></span><span style="width:4.5px;height:4.5px;border-radius:50%;background:var(--gold)"></span>
  </div>
  <div class="dots" style="left:284px;top:167px;grid-template-columns:repeat(4,1.4px)"><i></i><i></i><i></i><i></i></div>
</section>

<section class="slide c2 r1">
  <div class="abs teal" style="left:0;top:0;width:106px;height:180px"></div>
  <div class="bars" style="top:19px;border-color:#fff"></div>
  <h2 class="ttl white abs" style="left:21px;top:14px">Contents.</h2>
  <p class="bd white abs" style="left:21px;top:102px;width:60px;font-size:3.8px">Lorem ipsum dolor sit amet, consectetuer adipiscing elit, sed diam nonummy nibh euismod tincid</p>
  <div class="dots" style="left:52px;top:147px;grid-template-columns:repeat(4,1.4px)"><i style="background:#fff"></i><i style="background:#fff"></i><i style="background:#fff"></i><i style="background:#fff"></i></div>
  <div class="abs" style="left:134px;top:22px;width:170px">
    <div style="display:flex;gap:4px;margin-bottom:11px"><span class="num">1.</span><div><div class="hd">Lorem Ipsum</div><p class="bd">Lorem ipsum dolor sit amet, consectetuer adipiscing elit, sed do eiusmod tempor incididunt ut labore et dolore magna aliqua.</p></div></div>
    <div style="display:flex;gap:4px;margin-bottom:11px"><span class="num">2.</span><div><div class="hd">Lorem Ipsum</div><p class="bd">Lorem ipsum dolor sit amet, consectetuer adipiscing elit, sed diam nonummy nibh euismod tincid</p></div></div>
    <div style="display:flex;gap:4px;margin-bottom:11px"><span class="num">3.</span><div><div class="hd">Lorem Ipsum</div><p class="bd">Lorem ipsum dolor sit amet, consectetuer adipiscing elit, sed diam nonummy nibh euismod tincid</p></div></div>
    <div style="display:flex;gap:4px"><span class="num">4.</span><div><div class="hd">Lorem Ipsum</div><p class="bd">Lorem ipsum dolor sit amet, consectetuer adipiscing elit, sed diam nonummy nibh euismod tincid</p></div></div>
  </div>
  <div class="web">www.website.com</div>
</section>

<section class="slide c3 r1">
  <div class="abs teal" style="left:234px;top:0;width:86px;height:180px"></div>
  <div class="bars" style="top:19px"></div>
  <h2 class="ttl abs" style="left:21px;top:14px">About Us.</h2>
  <div class="dots" style="left:164px;top:16px;grid-template-columns:repeat(4,1.4px)"><i></i><i></i><i></i><i></i></div>
  <div class="photo" role="img" aria-label="Smiling baseball player in a red jersey at a stadium" style="left:194px;top:28px;width:114px;height:123px;background:linear-gradient(160deg,#6f94c4,#a9c4e0 45%,#b22a2a 75%,#8e1c1c)"></div>
  <div class="ring" style="left:180px;top:139px;width:25px;height:25px"></div>
  <div class="abs" style="left:25px;top:50px;width:150px">
    <div style="display:flex;gap:4px;margin-bottom:14px"><span class="num">1.</span><div><div class="hd">Lorem Ipsum</div><p class="bd">Lorem ipsum dolor sit amet, consectetuer adipiscing elit, sed diam nonummy nibh euismod tincidunt ut laoreet dolore.</p><p class="bd" style="margin-top:3px">Lorem ipsum dolor sit amet, cons ectetuer adipiscing elit, sed diam nonummy nibh euismod tincidunt ut laoreet dolor.</p></div></div>
    <div style="display:flex;gap:4px"><span class="num">2.</span><div><div class="hd">Lorem Ipsum</div><p class="bd">Lorem ipsum dolor sit amet, consectetuer adipiscing elit, sed diam nonummy nibh euismod tincidunt ut laoreet dolore magna aliquam erat volutpat. Ut wisi enim ad minim.</p></div></div>
  </div>
  <div class="web" style="color:#fff">www.website.com</div>
</section>

<!-- Row 2 -->
<section class="slide c1 r2">
  <div class="abs teal" style="left:0;top:0;width:106px;height:180px"></div>
  <div class="bars" style="top:19px;border-color:#fff"></div>
  <h2 class="ttl white abs" style="left:21px;top:14px">Agenda.</h2>
  <p class="bd white abs" style="left:21px;top:112px;width:60px;font-size:3.8px">Lorem ipsum dolor sit amet, consectetuer adipiscing elit, sed diam nonummy nibh euismod tincid</p>
  <div class="dots" style="left:90px;top:159px;grid-template-columns:repeat(8,1.4px)"><i></i><i></i><i></i><i></i><i></i><i></i><i></i><i></i></div>
  <div class="dots" style="left:144px;top:18px;grid-template-columns:repeat(4,1.4px)"><i></i><i></i><i></i><i></i></div>
  <div class="dots" style="left:297px;top:125px;grid-template-columns:repeat(2,1.4px);gap:3px"><i></i><i></i><i></i><i></i><i></i><i></i></div>
  <div class="icon" style="left:150px;top:23px;width:24px;height:24px"><svg width="10" height="10" viewBox="0 0 10 10"><rect x="2" y="1" width="6" height="8" fill="none" stroke="#fff"/><path d="M3.5 4h3M3.5 6h3" stroke="#fff" stroke-width=".8"/></svg></div>
  <div class="icon" style="left:230px;top:23px;width:24px;height:24px"><svg width="10" height="10" viewBox="0 0 10 10"><path d="M2 9V6M4 9V3M6 9V5M8 9V2" stroke="#fff" stroke-width="1.3"/></svg></div>
  <div class="icon" style="left:150px;top:99px;width:24px;height:24px"><svg width="10" height="10" viewBox="0 0 10 10"><path d="M1 2h8v5H4L2 9V7H1z" fill="#fff"/></svg></div>
  <div class="icon" style="left:230px;top:99px;width:24px;height:24px"><svg width="10" height="10" viewBox="0 0 10 10"><path d="M2 1h6v3a3 3 0 0 1-6 0zM4 7h2v1.5H7V9H3v-.5h1z" fill="#fff"/></svg></div>
  <div class="abs center" style="left:127px;top:52px;width:70px"><div class="hd">Lorem ipsum</div><p class="bd">Lorem ipsum dolor sit amet, consectetuer adipiscing elit, sed diam nonummy nibh euismod tincidunt ut</p></div>
  <div class="abs center" style="left:207px;top:52px;width:70px"><div class="hd">Lorem ipsum</div><p class="bd">Lorem ipsum dolor sit amet, consectetuer adipiscing elit, sed diam nonummy nibh euismod</p></div>
  <div class="abs center" style="left:122px;top:124px;width:80px"><div class="hd">Lorem ipsum</div><p class="bd">unt ut dolore magna aliquam erat volutpat. Ut wisi enim ad minim veniam</p></div>
  <div class="abs center" style="left:202px;top:124px;width:80px"><div class="hd">Lorem ipsum</div><p class="bd">nibh euismod tincidunt ut dolore magna aliquam erat volutpat. Ut wisi enim ad minim veniam</p></div>
  <div class="web">www.website.com</div>
</section>

<section class="slide c2 r2">
  <div class="abs teal" style="left:16px;top:13px;width:289px;height:154px"></div>
  <div class="abs" role="img" aria-label="Faint world map backdrop" style="left:45px;top:22px;width:230px;height:135px;border-radius:40%;background:radial-gradient(ellipse,rgba(0,120,95,.35),rgba(0,120,95,0) 70%)"></div>
  <div class="abs center" style="left:16px;top:62px;width:289px">
    <div style="font-family:'Playfair Display',serif;font-weight:900;color:#fff;font-size:15.5px;letter-spacing:2px;line-height:1.1">SECTION BREAK</div>
    <div style="font-family:'Playfair Display',serif;font-weight:900;color:var(--gold);font-size:15.5px;letter-spacing:2px;line-height:1.1">SLIDE TITLE</div>
    <p style="font-size:4.2px;color:#fff;margin:6px auto 0;width:190px;line-height:1.4">Lorem ipsum dolor sit amet, consectetuer adipiscing elit, sed diam nonummy nibh euismod tincid</p>
  </div>
</section>

<section class="slide c3 r2">
  <div class="bars" style="top:19px"></div>
  <h2 class="ttl abs" style="left:21px;top:14px">Make Your Title.</h2>
  <div class="abs teal" style="left:0;top:67px;width:320px;height:87px"></div>
  <div class="abs" style="left:0;top:38px;width:320px;display:flex;justify-content:space-around;padding:0 22px">
    <div class="center" style="width:84px">
      <div style="margin:10px auto 0;width:36px;height:36px;border-radius:50%;background:#fff;border:2px solid var(--gold);display:flex;align-items:center;justify-content:center;font-family:'Playfair Display',serif;font-weight:900;color:var(--gold);font-size:12px">01.</div>
      <div style="font-family:'Playfair Display',serif;font-weight:900;color:var(--gold-dark);font-size:7px;margin-top:6px">Lorem ipsum</div>
      <p class="bd white" style="font-size:3.8px">Lorem ipsum dolor sit amet, consectetuer adipiscing elit, sed diam nonummy nibh euismod tincidunt ut laoreet dolore magna volutpat.</p>
    </div>
    <div class="center" style="width:84px">
      <div style="margin:10px auto 0;width:36px;height:36px;border-radius:50%;background:#fff;border:2px solid var(--gold);display:flex;align-items:center;justify-content:center;font-family:'Playfair Display',serif;font-weight:900;color:var(--gold);font-size:12px">02.</div>
      <div style="font-family:'Playfair Display',serif;font-weight:900;color:var(--gold-dark);font-size:7px;margin-top:6px">Lorem ipsum</div>
      <p class="bd white" style="font-size:3.8px">Lorem ipsum dolor sit amet, consectetuer adipiscing elit, sed diam nonummy nibh euismod tincidunt ut laoreet dolore magna volutpat.</p>
    </div>
    <div class="center" style="width:84px">
      <div style="margin:10px auto 0;width:36px;height:36px;border-radius:50%;background:#fff;border:2px solid var(--gold);display:flex;align-items:center;justify-content:center;font-family:'Playfair Display',serif;font-weight:900;color:var(--gold);font-size:12px">03.</div>
      <div style="font-family:'Playfair Display',serif;font-weight:900;color:var(--gold-dark);font-size:7px;margin-top:6px">Lorem ipsum</div>
      <p class="bd white" style="font-size:3.8px">Lorem ipsum dolor sit amet, consectetuer adipiscing elit, sed diam nonummy nibh euismod tincidunt ut laoreet dolore magna volutpat.</p>
    </div>
  </div>
  <div class="web">www.website.com</div>
</section>

<!-- Row 3 -->
<section class="slide c1 r3">
  <div class="bars" style="top:19px"></div>
  <h2 class="ttl abs" style="left:21px;top:14px;line-height:1.45">Lorem Ipsum<br>Dolor Sit<br>Ametkeeper.</h2>
  <div class="abs teal" style="left:0;top:77px;width:122px;height:75px;padding:9px 12px 0 21px">
    <p class="bd white" style="font-size:3.8px">Lorem ipsum dolor sit amet, consectetuer adipiscing elit, sed diam nonummy nibh euismod tincidunt erat volutpat.</p>
    <p class="bd white" style="font-size:3.8px;margin-top:4px">Ut wisi enim ad minim veniam, quis nostrud exerci tation ullamcorper suscipit lobortis nisl ut aliquip ex ea commodo consequat.</p>
  </div>
  <div class="abs" style="left:135px;top:28px;width:170px">
    <div style="display:flex;gap:10px;align-items:center;margin-bottom:15px"><div class="icon" style="position:static;width:26px;height:26px;flex:none"><svg width="12" height="10" viewBox="0 0 12 10"><circle cx="6" cy="3" r="2" fill="#fff"/><circle cx="2.5" cy="4" r="1.5" fill="#fff"/><circle cx="9.5" cy="4" r="1.5" fill="#fff"/><path d="M2 9a4 4 0 0 1 8 0z" fill="#fff"/></svg></div><div><div class="hd" style="font-size:6.6px">We Before Me</div><p class="bd">ipsum dolor sit amet, cons ectetuer adipiscing elit, sed diam nonummy nibh euismod tincidunt ut laoreet</p></div></div>
    <div style="display:flex;gap:10px;align-items:center;margin-bottom:15px"><div class="icon" style="position:static;width:26px;height:26px;flex:none"><svg width="12" height="12" viewBox="0 0 12 12"><circle cx="4" cy="2" r="1.4" fill="#fff"/><circle cx="8" cy="2" r="1.4" fill="#fff"/><path d="M2.5 4h3v8h-3zM6.5 4h3v8h-3z" fill="#fff"/></svg></div><div><div class="hd" style="font-size:6.6px">We Are Good People</div><p class="bd">ipsum dolor sit amet, cons ectetuer adipiscing elit, sed diam nonummy nibh euismod tincidunt ut laoreet dolore magna aliquam erat volutpat.</p></div></div>
    <div style="display:flex;gap:10px;align-items:center"><div class="icon" style="position:static;width:26px;height:26px;flex:none"><svg width="12" height="10" viewBox="0 0 12 10"><path d="M6 8 2.5 4.5a2 2 0 0 1 3.5-2 2 2 0 0 1 3.5 2z" fill="#fff"/><path d="M1 9h10" stroke="#fff"/></svg></div><div><div class="hd" style="font-size:6.6px">We Work with Heart</div><p class="bd">ipsum dolor sit amet, cons ectetuer adipiscing elit, sed diam nonummy nibh euismod tincidunt</p></div></div>
  </div>
  <div class="web">www.website.com</div>
</section>

<section class="slide c2 r3">
  <div class="bars" style="top:19px"></div>
  <h2 class="ttl abs" style="left:23px;top:15px;font-size:11px">Market<br>Opportunities</h2>
  <p class="bd abs" style="left:23px;top:47px;width:128px">Lorem ipsum dolor sit amet, consectetuer adipiscing elit, sed diam nonummy nibh euismod tincidunt ut laoreet dolore magna aliquam erat volutpat. Ut wisi enim ad minim veniam, quis nostrud exerci tation ullamcorper suscipit lobortis nisl ut aliquip ex ea commodo consequat. Duis autem vel eum iriure</p>
  <svg class="abs" style="left:20px;top:84px" width="112" height="86" viewBox="0 0 112 86">
    <text x="56" y="6" font-size="5" font-family="Montserrat" font-weight="500" text-anchor="middle" fill="#222">Series 1</text>
    <g stroke="#e2e2e2" stroke-width=".4"><line x1="12" y1="15" x2="110" y2="15"/><line x1="12" y1="26" x2="110" y2="26"/><line x1="12" y1="37" x2="110" y2="37"/><line x1="12" y1="48" x2="110" y2="48"/><line x1="12" y1="59" x2="110" y2="59"/><line x1="12" y1="70" x2="110" y2="70"/></g>
    <g font-size="4" font-family="Montserrat" fill="#222" text-anchor="end"><text x="8" y="17">5</text><text x="8" y="28">4</text><text x="8" y="39">3</text><text x="8" y="50">2</text><text x="8" y="61">1</text><text x="8" y="72">0</text></g>
    <rect x="17" y="24" width="11" height="46" fill="var(--teal)"/>
    <rect x="36" y="43" width="11" height="27" fill="var(--gold)"/>
    <rect x="55" y="31" width="11" height="39" fill="var(--teal)"/>
    <rect x="74" y="67" width="11" height="3" fill="var(--gold)"/>
    <g font-size="4" font-family="Montserrat" fill="#222" text-anchor="middle"><text x="22" y="80">1980</text><text x="41" y="80">1990</text><text x="60" y="80">2000</text><text x="79" y="80">2010</text></g>
  </svg>
  <div class="abs" style="left:197px;top:17px;font-size:7px;font-weight:600">Radial Bar Chart</div>
  <svg class="abs" style="left:180px;top:34px" width="102" height="102" viewBox="0 0 102 102">
    <circle cx="51" cy="51" r="45" fill="none" stroke="var(--ring)" stroke-width="9"/>
    <circle cx="51" cy="51" r="34" fill="none" stroke="var(--ring)" stroke-width="9"/>
    <circle cx="51" cy="51" r="23" fill="none" stroke="var(--ring)" stroke-width="9"/>
    <circle cx="51" cy="51" r="45" fill="none" stroke="var(--teal)" stroke-width="6" stroke-dasharray="192 300" transform="rotate(-90 51 51)"/>
    <circle cx="51" cy="51" r="34" fill="none" stroke="var(--gold)" stroke-width="6" stroke-dasharray="75 300" transform="rotate(-90 51 51)"/>
    <circle cx="51" cy="51" r="34" fill="none" stroke="var(--teal)" stroke-width="6" stroke-dasharray="0 75 75 300" transform="rotate(-90 51 51)"/>
    <circle cx="51" cy="51" r="23" fill="none" stroke="var(--gold)" stroke-width="6" stroke-dasharray="108 300" transform="rotate(-90 51 51)"/>
    <g font-size="3" font-family="Montserrat" fill="var(--teal)"><text x="4" y="32">68%</text><text x="30" y="75">35%</text></g>
    <g font-size="3" font-family="Montserrat" fill="var(--gold)"><text x="18" y="78">45%</text><text x="60" y="45">5%</text></g>
  </svg>
  <div class="abs" style="left:160px;top:141px;width:150px;display:flex;gap:14px">
    <div><div style="font-size:4.4px;font-weight:600"><span style="display:inline-block;width:4px;height:4px;border-radius:50%;background:var(--teal);margin-right:2px"></span>Lorem ipsum</div><p class="bd" style="font-size:2.6px;width:62px">Lorem ipsum dolor sit amet, consectetuer adipiscing elit, sed diam nonummy nibh euismod tincidunt ut laoreet</p></div>
    <div><div style="font-size:4.4px;font-weight:600"><span style="display:inline-block;width:4px;height:4px;border-radius:50%;background:var(--gold);margin-right:2px"></span>Lorem ipsum</div><p class="bd" style="font-size:2.6px;width:62px">Lorem ipsum dolor sit amet, consectetuer adipiscing elit, sed diam nonummy nibh euismod tincidunt ut laoreet</p></div>
  </div>
  <div class="web">www.website.com</div>
</section>

<section class="slide c3 r3">
  <div class="bars" style="top:19px"></div>
  <h2 class="ttl abs" style="left:23px;top:15px;font-size:12px">Our<br>Company</h2>
  <p class="bd abs" style="left:23px;top:50px;width:96px">Lorem ipsum dolor sit amet, consectetuer adipiscing elit, sed diam nonummy nibh euismod tincidunt ut laoreet dolore magna aliquam erat volutpat. Ut wisi enim ad minim veniam, quis nostrud exerci tation ullamcorper suscipit lobortis nisl ut aliquip ex ea commodo consequat. Duis autem vel eum iriure dolor in hendrerit i</p>
  <p class="bd abs" style="left:23px;top:106px;width:96px">Lorem ipsum dolor sit amet, consectetuer adipiscing elit, sed diam nonummy nibh . Lorem ipsum dolor sit amet, consectetuer adipiscing elit, sed diam nonummy nibh euismod tincidunt ut laoreet dolore magna aliquam erat volutpat. Ut wisi consectetuer adipiscing elit, sed diam nonummy nibh euismod tincidunt ut laoreet dolore magna</p>
  <svg class="abs" style="left:134px;top:26px" width="170" height="96" viewBox="0 0 170 96">
    <text x="95" y="6" font-size="5" font-family="Montserrat" font-weight="600" text-anchor="middle" fill="#222">Volume</text>
    <g stroke="#e2e2e2" stroke-width=".4"><line x1="16" y1="12" x2="168" y2="12"/><line x1="16" y1="20.5" x2="168" y2="20.5"/><line x1="16" y1="29" x2="168" y2="29"/><line x1="16" y1="37.5" x2="168" y2="37.5"/><line x1="16" y1="46" x2="168" y2="46"/><line x1="16" y1="54.5" x2="168" y2="54.5"/><line x1="16" y1="63" x2="168" y2="63"/><line x1="16" y1="71.5" x2="168" y2="71.5"/><line x1="16" y1="80" x2="168" y2="80"/></g>
    <g font-size="4" font-family="Montserrat" fill="#222" text-anchor="end"><text x="12" y="13.5">160</text><text x="12" y="22">140</text><text x="12" y="30.5">120</text><text x="12" y="39">100</text><text x="12" y="47.5">80</text><text x="12" y="56">60</text><text x="12" y="64.5">40</text><text x="12" y="73">20</text><text x="12" y="81.5">0</text></g>
    <rect x="26" y="50" width="14" height="30" fill="var(--gold)"/>
    <rect x="62" y="29" width="14" height="51" fill="var(--teal)"/>
    <rect x="98" y="17" width="14" height="63" fill="var(--gold)"/>
    <rect x="134" y="23" width="14" height="57" fill="var(--teal)"/>
    <g font-size="4" font-family="Montserrat" fill="#222" text-anchor="middle"><text x="33" y="92">JAN</text><text x="69" y="92">FEB</text><text x="105" y="92">MAR</text><text x="141" y="92">APR</text></g>
  </svg>
  <div class="abs" style="left:135px;top:131px;width:170px;display:flex;gap:16px">
    <div><div style="font-size:5px;font-weight:600"><span style="display:inline-block;width:4.5px;height:4.5px;border-radius:50%;background:var(--teal);margin-right:2px"></span>Lorem ipsum</div><p class="bd" style="font-size:2.6px;width:70px;padding-left:8px">Lorem ipsum dolor sit amet, consectetuer adipiscing elit, sed diam nonummy nibh euismod tincidunt ut laoreet</p></div>
    <div><div style="font-size:5px;font-weight:600"><span style="display:inline-block;width:4.5px;height:4.5px;border-radius:50%;background:var(--gold);margin-right:2px"></span>Lorem ipsum</div><p class="bd" style="font-size:2.6px;width:70px;padding-left:8px">Lorem ipsum dolor sit amet, consectetuer adipiscing elit, sed diam nonummy nibh euismod tincidunt ut laoreet</p></div>
  </div>
  <div class="web">www.website.com</div>
</section>

<!-- Row 4 -->
<section class="slide c1 r4">
  <div class="bars" style="top:19px"></div>
  <h2 class="ttl abs" style="left:21px;top:14px;font-size:12px;line-height:1.45">Subject<br>Title.</h2>
  <div class="abs teal" style="left:0;top:60px;width:106px;height:92px;padding:9px 34px 0 16px">
    <p style="font-size:3.8px;line-height:1.3;color:#fff;font-weight:600">Lorem ipsum dolor sit amet, consectetuer elit, sed diam nonummy nibh euismod tincidunt ut laoreet dolore magna aliquam erat volutpat. Ut wisi enim ad minim veniam, quis nostrud exerci tation ullamcorper suscipit lobortis nisl ut aliquip ex ea commodo</p>
  </div>
  <div class="photo" role="img" aria-label="Factory workers sewing caps on a production line" style="left:82px;top:0;width:73px;height:120px;background:linear-gradient(170deg,#8a8f96,#4f5a6e 50%,#2c3340)"></div>
  <div class="photo" role="img" aria-label="Worker operating an industrial sewing machine" style="left:164px;top:61px;width:66px;height:107px;background:linear-gradient(170deg,#c9ced6,#7d8aa3 45%,#3a3550)"></div>
  <div class="abs" style="left:168px;top:18px;width:140px"><div class="hd" style="color:#1d3b8a"><span class="num" style="color:#d83a2c;font-size:8px">1.</span> Lorem Ipsum</div><p class="bd" style="padding-left:8px">Lorem ipsum dolor sit amet, consectetur adipiscing elit, sed do eiusmod tempor incididunt ut labore et dolore magna aliqua.</p></div>
  <div class="abs" style="left:238px;top:68px;width:72px"><div class="hd" style="color:#1d3b8a"><span class="num" style="color:#d83a2c;font-size:8px">2.</span> Lorem Ipsum</div><p class="bd" style="padding-left:9px">Lorem ipsum dolor sit amet, consectetur adipiscing elit, sed do eiusmod tempor incididunt ut labore et dolore magna aliqua. tincid</p></div>
  <div class="abs" style="left:238px;top:119px;width:72px"><div class="hd" style="color:#1d3b8a"><span class="num" style="color:#d83a2c;font-size:8px">3.</span> Lorem Ipsum</div><p class="bd" style="padding-left:9px">Lorem ipsum dolor sit amet, consectetuer adipiscing elit, sed diam nonummy nibh euismod</p></div>
  <div class="web">www.website.com</div>
</section>

<section class="slide c2 r4">
  <div class="bars" style="top:19px"></div>
  <h2 class="ttl abs" style="left:21px;top:14px">Text Added Here</h2>
  <div class="abs" style="left:27px;top:52px;display:flex;gap:11px">
    <div class="teal" style="width:58px;height:81px;padding:20px 8px 0;position:relative"><div class="icon" style="left:17px;top:-12px;width:24px;height:24px;border:2px solid #fff"><svg width="9" height="9" viewBox="0 0 10 10"><rect x="1" y="2" width="8" height="6" fill="none" stroke="#fff"/></svg></div><div style="font-size:5px;font-weight:700;color:#fff">Lorem ipsum</div><p class="bd white" style="font-size:3px">Lorem ipsum dolor sit amet, cons ectetuer adipiscing elit, sed diam nonummy nibh euismod tincidunt ut laoreet</p><p class="bd white" style="font-size:3px;margin-top:3px">ipsum dolor sit amet, cons ectetuer adipiscing elit, sed diam nonummy nibh euismod tincidunt ut laoreet ipsum dolor sit amet, cons ectetuer</p></div>
    <div style="width:58px;height:81px;padding:20px 8px 0;position:relative;background:var(--grey-card)"><div class="icon" style="left:17px;top:-12px;width:24px;height:24px;border:2px solid #fff"><svg width="9" height="9" viewBox="0 0 10 10"><rect x="1" y="1" width="8" height="6" fill="none" stroke="#fff"/><path d="M3 9h4" stroke="#fff"/></svg></div><div style="font-size:5px;font-weight:700;color:#fff">Lorem ipsum</div><p class="bd white" style="font-size:3px">Lorem ipsum dolor sit amet, cons ectetuer adipiscing elit, sed diam nonummy nibh euismod tincidunt ut laoreet</p><p class="bd white" style="font-size:3px;margin-top:3px">ipsum dolor sit amet, cons ectetuer adipiscing elit, sed diam nonummy nibh euismod tincidunt ut laoreet ipsum dolor sit amet, cons ectetuer</p></div>
    <div class="teal" style="width:58px;height:81px;padding:20px 8px 0;position:relative"><div class="icon" style="left:17px;top:-12px;width:24px;height:24px;border:2px solid #fff"><svg width="10" height="8" viewBox="0 0 10 8"><path d="M0 3 5 1l5 2-5 2z" fill="#fff"/><path d="M2 4v2.5h6V4" fill="none" stroke="#fff"/></svg></div><div style="font-size:5px;font-weight:700;color:#fff">Lorem ipsum</div><p class="bd white" style="font-size:3px">Lorem ipsum dolor sit amet, cons ectetuer adipiscing elit, sed diam nonummy nibh euismod tincidunt ut laoreet</p><p class="bd white" style="font-size:3px;margin-top:3px">ipsum dolor sit amet, cons ectetuer adipiscing elit, sed diam nonummy nibh euismod tincidunt ut laoreet ipsum dolor sit amet, cons ectetuer</p></div>
    <div style="width:58px;height:81px;padding:20px 8px 0;position:relative;background:var(--grey-card)"><div class="icon" style="left:17px;top:-12px;width:24px;height:24px;border:2px solid #fff"><svg width="9" height="9" viewBox="0 0 10 10"><rect x="1" y="2" width="8" height="7" fill="none" stroke="#fff"/><path d="M3 5h4" stroke="#fff"/></svg></div><div style="font-size:5px;font-weight:700;color:#fff">Lorem ipsum</div><p class="bd white" style="font-size:3px">Lorem ipsum dolor sit amet, cons ectetuer adipiscing elit, sed diam nonummy nibh euismod tincidunt ut laoreet</p><p class="bd white" style="font-size:3px;margin-top:3px">ipsum dolor sit amet, cons ectetuer adipiscing elit, sed diam nonummy nibh euismod tincidunt ut laoreet ipsum dolor sit amet, cons ectetuer</p></div>
  </div>
  <div class="abs" style="left:27px;top:143px;font-size:11px;font-weight:700;color:#e0262c">+ 35k</div>
  <p class="bd abs" style="left:27px;top:157px;width:215px;font-size:3px">Lorem ipsum dolor sit amet, consectetuer adipiscing elit, sed diam nonummy nibh euismod tincidunt ut laoreet dolore magna aliquam erat volutpat. Ut wisi enim ad minim veniam, quis nostrud exerci tation ullamcorper</p>
  <div class="web">www.website.com</div>
</section>

<section class="slide c3 r4">
  <div class="abs teal" style="left:0;top:0;width:320px;height:84px"></div>
  <div class="bars" style="top:19px;border-color:#fff"></div>
  <h2 class="ttl white abs" style="left:21px;top:14px">Text Added Here</h2>
  <div class="abs" role="img" aria-label="Close-up of an embroidered cap on a machine" style="left:36px;top:51px;width:68px;height:68px;border-radius:50%;border:3px solid #fff;background:radial-gradient(circle at 45% 40%,#2d4a8a,#1b1f28 70%)"></div>
  <div class="abs" role="img" aria-label="Smiling coach in a yellow team jersey" style="left:122px;top:51px;width:68px;height:68px;border-radius:50%;border:3px solid #fff;background:radial-gradient(circle at 50% 70%,#f0c330,#c7a37a 45%,#7b8a9a)"></div>
  <div class="abs" role="img" aria-label="Pile of numbered team caps" style="left:217px;top:51px;width:68px;height:68px;border-radius:50%;border:3px solid #fff;background:radial-gradient(circle,#c2283a,#2a2f3c 60%,#1a7a46)"></div>
  <div class="abs" style="left:24px;top:126px;width:280px;display:flex;justify-content:space-between">
    <div style="width:80px"><div class="hd" style="font-size:6.4px;color:#444">Laoreet Dolore</div><p class="bd" style="font-size:3px">Lorem ipsum dolor sit amet, consectetuer adipiscing elit, sed diam nonummy nibh euismod tincidunt ut</p></div>
    <div style="width:80px"><div class="hd" style="font-size:6.4px;color:#444">Laoreet Dolore</div><p class="bd" style="font-size:3px">Lorem ipsum dolor sit amet, consectetuer adipiscing elit, sed diam nonummy nibh euismod tincidunt ut</p></div>
    <div style="width:80px"><div class="hd" style="font-size:6.4px;color:#444">Laoreet Dolore</div><p class="bd" style="font-size:3px">Lorem ipsum dolor sit amet, consectetuer adipiscing elit, sed diam nonummy nibh euismod tincidunt ut</p></div>
  </div>
  <div class="web">www.website.com</div>
</section>

<!-- Row 5 -->
<section class="slide c1 r5">
  <div class="abs teal" style="left:0;top:0;width:108px;height:180px"></div>
  <div class="bars" style="top:19px;border-color:#fff"></div>
  <h2 class="ttl white abs" style="left:21px;top:14px">Summary</h2>
  <div class="abs" style="left:21px;top:37px;width:76px">
    <p class="bd white" style="font-size:3.8px">Lorem ipsum dolor sit amet, consectetuer adipiscing elit, sed diam nonummy nibh .</p>
    <p class="bd white" style="font-size:3.8px;margin-top:4px">Ut wisi enim ad minim veniam, quis nostrud exerci tation ullamcorper suscipit lobortis.</p>
    <div style="margin-top:10px;display:grid;gap:8px">
      <div style="display:flex;gap:4px"><span style="width:4px;height:4px;border-radius:50%;background:var(--gold);margin-top:2px;flex:none"></span><div><div style="font-size:5.4px;font-weight:600;color:var(--gold)">Lorem ipsum</div><p class="bd white" style="font-size:2.6px">Lorem ipsum dolor sit amet, consectetuer adipiscing elit, sed diam nonummy nibh euismod</p></div></div>
      <div style="display:flex;gap:4px"><span style="width:4px;height:4px;border-radius:50%;background:var(--gold);margin-top:2px;flex:none"></span><div><div style="font-size:5.4px;font-weight:600;color:var(--gold)">Lorem ipsum</div><p class="bd white" style="font-size:2.6px">Lorem ipsum dolor sit amet, consectetuer adipiscing elit, sed diam nonummy nibh euismod</p></div></div>
      <div style="display:flex;gap:4px"><span style="width:4px;height:4px;border-radius:50%;background:var(--gold);margin-top:2px;flex:none"></span><div><div style="font-size:5.4px;font-weight:600;color:var(--gold)">Lorem ipsum</div><p class="bd white" style="font-size:2.6px">Lorem ipsum dolor sit amet, consectetuer adipiscing elit, sed diam nonummy nibh euismod</p></div></div>
    </div>
  </div>
  <div class="dots" style="left:80px;top:164px;grid-template-columns:repeat(4,1.4px)"><i style="background:#fff"></i><i style="background:#fff"></i><i style="background:#fff"></i><i style="background:#fff"></i></div>
  <div class="dots" style="left:122px;top:16px;grid-template-columns:repeat(4,1.4px)"><i></i><i></i><i></i><i></i></div>
  <svg class="abs" style="left:108px;top:20px" width="212" height="150" viewBox="0 0 212 150">
    <path d="M112 50 A52 52 0 0 0 22 52" fill="none" stroke="#2a2a2a" stroke-width="2"/>
    <path d="M24 44 L19 62 L14 44" fill="none" stroke="#2a2a2a" stroke-width="2"/>
    <path d="M18 84 C20 130 60 140 100 130 C130 122 148 104 130 86 C118 74 118 60 112 50" fill="none" stroke="#2a2a2a" stroke-width="2"/>
    <circle cx="18" cy="84" r="2.5" fill="#2a2a2a"/>
    <circle cx="171" cy="36" r="0" />
    <circle cx="72" cy="38" r="20" fill="#fff" stroke="var(--gold)" stroke-width="4"/>
    <circle cx="72" cy="38" r="12" fill="none" stroke="var(--gold)" stroke-width="1.5"/>
    <path d="M69 40l-3 3M70 36a3 3 0 1 0 .1 0" stroke="var(--teal)" stroke-width="1.2" fill="none"/>
    <circle cx="132" cy="86" r="15" fill="#fff" stroke="var(--teal)" stroke-width="4"/>
    <circle cx="132" cy="86" r="6" fill="var(--teal)"/>
    <circle cx="42" cy="112" r="10" fill="#fff" stroke="var(--teal)" stroke-width="3"/>
    <circle cx="42" cy="112" r="3" fill="var(--gold)"/>
    <circle cx="103" cy="129" r="11" fill="#fff" stroke="var(--gold)" stroke-width="3"/>
    <path d="M103 124v9M99 130a4 3 0 0 0 8 0" stroke="var(--teal)" stroke-width="1.2" fill="none"/>
    <path d="M92 20 L100 18 L104 22" stroke="var(--gold)" stroke-width=".6" fill="none"/><text x="106" y="23" font-size="3.6" fill="var(--gold)" font-family="Montserrat">85%</text>
    <text x="96" y="79" font-size="3.6" fill="var(--gold)" font-family="Montserrat">80%</text>
    <path d="M52 112 L60 105 L64 105" stroke="var(--teal)" stroke-width=".6" fill="none"/><text x="66" y="107" font-size="3.6" fill="var(--teal)" font-family="Montserrat">50%</text>
    <text x="114" y="136" font-size="3.6" fill="var(--gold)" font-family="Montserrat">75%</text>
    <g fill="var(--teal)"><rect x="34" y="53" width="2" height="9"/><rect x="37" y="56" width="2" height="6"/><rect x="40" y="51" width="2" height="11"/><rect x="43" y="58" width="2" height="4"/></g>
    <text x="26" y="68" font-size="4.6" font-weight="600" font-family="Montserrat" fill="#222">MAIN TITLE</text>
    <text x="26" y="72" font-size="2.4" font-family="Montserrat" fill="#999">Lorem ipsum dolor sit amet,</text>
    <text x="26" y="75" font-size="2.4" font-family="Montserrat" fill="#999">consectetuer adipiscing elit</text>
    <g font-family="Montserrat"><text x="126" y="36" font-size="4.4" font-weight="600" fill="#222">Your Title</text><text x="122" y="40" font-size="2.2" fill="#999">Lorem ipsum dolor sit amet,</text><text x="122" y="43" font-size="2.2" fill="#999">consectetuer adipiscing</text>
    <text x="163" y="78" font-size="4.4" font-weight="600" fill="#222">Your Title</text><text x="160" y="82" font-size="2.2" fill="#999">Lorem ipsum dolor sit amet,</text><text x="160" y="85" font-size="2.2" fill="#999">consectetuer adipiscing</text>
    <text x="2" y="104" font-size="4.4" font-weight="600" fill="#222">Your Title</text><text x="0" y="108" font-size="2.2" fill="#999">Lorem ipsum dolor sit amet,</text><text x="0" y="111" font-size="2.2" fill="#999">consectetuer adipiscing</text>
    <text x="153" y="118" font-size="4.4" font-weight="600" fill="#222">Your Title</text><text x="150" y="122" font-size="2.2" fill="#999">Lorem ipsum dolor sit amet,</text><text x="150" y="125" font-size="2.2" fill="#999">consectetuer adipiscing</text></g>
  </svg>
  <div class="web">www.website.com</div>
</section>

<section class="slide c2 r5">
  <div class="bars" style="top:19px"></div>
  <h2 class="ttl abs" style="left:21px;top:14px">Our Timeline</h2>
  <div class="dots" style="left:299px;top:16px;grid-template-columns:1.4px;gap:2.4px"><i></i><i></i><i></i><i></i><i></i><i></i><i></i><i></i></div>
  <div class="abs" style="left:61px;top:38px;width:.8px;height:82px;background:#2a2a2a"></div>
  <div class="abs" style="left:59.5px;top:37px;width:3px;height:3px;border-radius:50%;background:#2a2a2a"></div>
  <div class="abs" style="left:30px;top:47px;display:grid;gap:7px;font-size:6px;font-weight:600">
    <div style="display:flex;align-items:center;height:17px;gap:4px"><span style="width:5px;height:5px;border-radius:50%;background:var(--gold)"></span>2019</div>
    <div style="display:flex;align-items:center;height:17px;gap:4px"><span style="width:5px;height:5px;border-radius:50%;background:var(--gold)"></span>2020</div>
    <div style="display:flex;align-items:center;height:17px;gap:4px"><span style="width:5px;height:5px;border-radius:50%;background:var(--gold)"></span>2021</div>
  </div>
  <div class="abs" style="left:62px;top:47px;display:grid;gap:7px;font-size:4.8px;color:#fff">
    <div style="display:flex;height:17px;line-height:17px;text-align:center"><span style="width:30px;background:var(--teal)">20%</span><span style="width:42px;background:var(--gold)">40%</span><span style="width:29px;background:var(--teal)">10%</span><span style="width:105px;background:var(--gold)">90%</span></div>
    <div style="display:flex;height:17px;line-height:17px;text-align:center"><span style="width:73px;background:var(--teal)">50%</span><span style="width:52px;background:var(--gold)">30%</span><span style="width:42px;background:var(--teal)">20%</span><span style="width:39px;background:var(--gold)">20%</span></div>
    <div style="display:flex;height:17px;line-height:17px;text-align:center"><span style="width:42px;background:var(--gold)">30%</span><span style="width:62px;background:var(--teal)">60%</span><span style="width:20px;background:var(--gold)">10%</span><span style="width:82px;background:var(--teal)">70%</span></div>
  </div>
  <svg class="abs" style="left:55px;top:116px" width="222" height="16" viewBox="0 0 222 16">
    <line x1="7" y1="4" x2="213" y2="4" stroke="#2a2a2a" stroke-width=".8"/>
    <g fill="#2a2a2a"><circle cx="7" cy="4" r="1.6"/><circle cx="27.6" cy="4" r="1.6"/><circle cx="48.2" cy="4" r="1.6"/><circle cx="68.8" cy="4" r="1.6"/><circle cx="89.4" cy="4" r="1.6"/><circle cx="110" cy="4" r="1.6"/><circle cx="130.6" cy="4" r="1.6"/><circle cx="151.2" cy="4" r="1.6"/><circle cx="171.8" cy="4" r="1.6"/><circle cx="192.4" cy="4" r="1.6"/><circle cx="213" cy="4" r="1.6"/></g>
    <g font-size="4.4" font-family="Montserrat" fill="#222" text-anchor="middle"><text x="7" y="13">0%</text><text x="27.6" y="13">10%</text><text x="48.2" y="13">20%</text><text x="68.8" y="13">30%</text><text x="89.4" y="13">40%</text><text x="110" y="13">50%</text><text x="130.6" y="13">60%</text><text x="151.2" y="13">70%</text><text x="171.8" y="13">80%</text><text x="192.4" y="13">90%</text><text x="213" y="13">100%</text></g>
  </svg>
  <div class="abs" style="left:58px;top:139px;display:flex;gap:10px">
    <div style="width:48px"><div style="font-size:4.4px;font-weight:600;color:var(--teal)">Lorem ipsum</div><p class="bd" style="font-size:2.5px">Lorem ipsum dolor sit amet, consectetuer adipiscing elit, sed diam nonummy</p></div>
    <div style="width:48px"><div style="font-size:4.4px;font-weight:600;color:var(--gold-dark)">Lorem ipsum</div><p class="bd" style="font-size:2.5px">Lorem ipsum dolor sit amet, consectetuer adipiscing elit, sed diam nonummy</p></div>
    <div style="width:48px"><div style="font-size:4.4px;font-weight:600;color:var(--teal)">Lorem ipsum</div><p class="bd" style="font-size:2.5px">Lorem ipsum dolor sit amet, consectetuer adipiscing elit, sed diam nonummy</p></div>
    <div style="width:48px"><div style="font-size:4.4px;font-weight:600;color:var(--gold-dark)">Lorem ipsum</div><p class="bd" style="font-size:2.5px">Lorem ipsum dolor sit amet, consectetuer adipiscing elit, sed diam nonummy</p></div>
  </div>
  <div class="dots" style="left:15px;top:153px;grid-template-columns:repeat(4,1.4px)"><i></i><i></i><i></i><i></i></div>
  <div class="web">www.website.com</div>
</section>

<section class="slide c3 r5">
  <div class="bars" style="top:19px"></div>
  <h2 class="ttl abs" style="left:21px;top:14px">Text Added Here</h2>
  <div class="abs" style="left:32px;top:37px;width:270px;display:flex;gap:16px">
    <div style="flex:1"><div style="font-size:7px;font-weight:600;color:var(--teal)">1. Text Added Here</div><p class="bd" style="font-size:3px;margin-top:2px">Lorem ipsum dolor sit amet, cons ectetuer adipiscing elit, sed diam nonummy nibh euismod tincidunt ut laoreet dolore magna aliquam erat volutpat. Ut wisi enim ad minim veniam, quis nostrud exerci tation ullamcorper suscipit lobortis nisl ut aliquip ex ea commodo consequat.</p><p class="bd" style="font-size:3px;margin-top:3px">Lorem ipsum dolor sit amet, consectetuer adipiscing elit, sed diam nonummy nibh euismod tincidunt ut laoreet dolore magna aliquam erat volutpat. Ut wisi enim ad minim veniam, quis nostrud exerci tation ullamcorper suscipit lobortis nisl ut aliquip ex ea commodo consequat.</p></div>
    <div style="flex:1"><div style="font-size:7px;font-weight:600;color:var(--teal)">2. Text Added Here</div><p class="bd" style="font-size:3px;margin-top:2px">Lorem ipsum dolor sit amet, cons ectetuer adipiscing elit, sed diam nonummy nibh euismod tincidunt ut laoreet dolore magna aliquam erat volutpat. Ut wisi enim ad minim veniam, quis nostrud exerci tation ullamcorper suscipit lobortis nisl ut aliquip ex ea commodo consequat.</p><p class="bd" style="font-size:3px;margin-top:3px">Lorem ipsum dolor sit amet, consectetuer adipiscing elit, sed diam nonummy nibh euismod tincidunt ut laoreet dolore magna aliquam erat volutpat. Ut wisi enim ad minim veniam, quis nostrud exerci tation ullamcorper suscipit lobortis nisl ut aliquip ex ea commodo consequat.</p></div>
  </div>
  <div class="abs" style="left:38px;top:107px;display:grid;grid-template-columns:136px 110px;row-gap:11px">
    <div style="display:flex;gap:6px"><span style="width:12px;height:12px;background:var(--gold);color:#fff;font-size:6px;font-weight:700;display:flex;align-items:center;justify-content:center">1.</span><div><div style="font-size:6px;font-weight:500">Lorem ipsum</div><p class="bd" style="font-size:2.8px;width:80px">Lorem ipsum dolor sit amet, consectetuer adipiscing elit, sed diam nonummy nibh</p></div></div>
    <div style="display:flex;gap:6px"><span style="width:12px;height:12px;background:var(--teal);color:#fff;font-size:6px;font-weight:700;display:flex;align-items:center;justify-content:center">1.</span><div><div style="font-size:6px;font-weight:500">Lorem ipsum</div><p class="bd" style="font-size:2.8px;width:80px">Lorem ipsum dolor sit amet, consectetuer adipiscing elit, sed diam nonummy nibh</p></div></div>
    <div style="display:flex;gap:6px"><span style="width:12px;height:12px;background:var(--teal);color:#fff;font-size:6px;font-weight:700;display:flex;align-items:center;justify-content:center">2.</span><div><div style="font-size:6px;font-weight:500">Lorem ipsum</div><p class="bd" style="font-size:2.8px;width:80px">Lorem ipsum dolor sit amet, consectetuer adipiscing elit, sed diam nonummy nibh</p></div></div>
    <div style="display:flex;gap:6px"><span style="width:12px;height:12px;background:var(--gold);color:#fff;font-size:6px;font-weight:700;display:flex;align-items:center;justify-content:center">2.</span><div><div style="font-size:6px;font-weight:500">Lorem ipsum</div><p class="bd" style="font-size:2.8px;width:80px">Lorem ipsum dolor sit amet, consectetuer adipiscing elit, sed diam nonummy nibh</p></div></div>
  </div>
  <div class="web">www.website.com</div>
</section>

<!-- Row 6 -->
<section class="slide c1 r6">
  <div class="bars" style="top:19px"></div>
  <h2 class="ttl abs" style="left:21px;top:14px">Our Member</h2>
  <div class="dots" style="left:267px;top:35px;grid-template-columns:repeat(4,1.4px)"><i></i><i></i><i></i><i></i></div>
  <div class="abs teal" style="left:30px;top:88px;width:48px;height:77px;padding:20px 0 0 7px">
    <p style="font-size:5px;font-weight:600;color:#fff;line-height:1.3">Lorem<br>Ipsum<br>Dolor Sit<br>Amet,<br>Consec-<br>teteur<br>Adipiscing</p>
  </div>
  <div class="abs" role="img" aria-label="Member portrait placeholder" style="left:32px;top:42px;width:44px;height:44px;border-radius:50%;border:2px solid #fff;background:repeating-conic-gradient(#d5d5d5 0 25%,#f4f4f4 0 50%) 0 0/6px 6px"></div>
  <div class="abs" style="left:86px;top:56px;font-size:8.4px;font-weight:700;color:var(--gold)">YOUR NAME</div>
  <div class="abs" style="left:86px;top:67px;font-size:5.6px;color:#555">Position<span style="display:inline-block;width:30px;height:.5px;background:#555;vertical-align:middle;margin-left:2px"></span></div>
  <div class="abs" style="left:86px;top:82px;width:204px">
    <p class="bd" style="font-size:3.4px">Lorem ipsum dolor sit amet, consectetuer adipiscing elit, sed diam nonummy nibh euismod tincidunt ut laoreet dolore magna aliquam erat volutpat. Ut wisi enim ad minim veniam, quis nostrud exerci tation ullamcorper suscipit lobortis nisl ut aliquip ex ea commodo consequat. Duis autem vel eum iriure dolor in hendrerit in vulputate velit esse molestie consequat, vel illum dolore eu feugiat nulla facilisis at vero eros et accumsan et iusto odio dignissim qui blandit praesent luptatum zzril delenit augue duis dolore te feugait nulla facilisi.</p>
    <p class="bd" style="font-size:3.4px;margin-top:4px">Lorem ipsum dolor sit amet, cons ectetuer adipiscing elit, sed diam nonummy nibh euismod tincidunt ut laoreet dolore magna aliquam erat volutpat. Ut wisi enim ad minim veniam, quis nostrud exerci tation ullamcorper suscipit lobortis nisl ut aliquip ex ea commodo consequat. Lorem ipsum dolor sit amet, consectetuer adipiscing elit, sed diam nonummy nibh euismod tincidunt ut laoreet dolore magna aliquam erat volutpat. Ut wisi enim ad minim veniam, quis nostrud exerci tation ullamcorper suscipit lobortis nisl ut aliquip ex ea commodo consequat.</p>
  </div>
  <div class="dots" style="left:60px;top:167px;grid-template-columns:repeat(4,1.4px)"><i></i><i></i><i></i><i></i></div>
  <div class="web">www.website.com</div>
</section>

<section class="slide c2 r6">
  <div class="bars" style="top:19px"></div>
  <h2 class="ttl abs" style="left:21px;top:14px">Team Members.</h2>
  <p class="bd abs" style="left:21px;top:31px;width:250px;font-size:3.6px">Lorem ipsum dolor sit amet, consectetuer adipiscing elit, sed diam nonummy nibh euismod tincim veniam, quis nostrud exerci tation ullamcorper suscipit lobortis nisl ut aliquip ex ea commodo consequat. Duis autem</p>
  <div class="abs teal" style="left:0;top:85px;width:320px;height:72px"></div>
  <div class="abs" style="left:20px;top:55px;width:280px;display:flex;justify-content:space-between">
    <div class="center" style="width:80px"><div role="img" aria-label="Team member portrait" style="margin:0 auto;width:48px;height:48px;border-radius:50%;border:2px solid #fff;background:radial-gradient(circle at 50% 40%,#e3c1a6,#b9c4cc 70%)"></div><div style="font-size:7px;font-weight:700;margin-top:3px;color:#1f2a2a">JOHN SMITH</div><p class="bd white" style="font-size:2.8px">ipsum dolor sit amet, cons ectetuer adipiscing elit, sed diam nonummy nibh euismod tincidunt ut laoreet dolore magna aliquam erat volutpat. Ut wisi enim ad minim veniam, quis nostrud</p></div>
    <div class="center" style="width:80px"><div role="img" aria-label="Team member portrait" style="margin:0 auto;width:48px;height:48px;border-radius:50%;border:2px solid #fff;background:radial-gradient(circle at 50% 40%,#c99a7d,#3a2a26 60%,#d8d8d8)"></div><div style="font-size:7px;font-weight:700;margin-top:3px;color:#1f2a2a">MILLIE SMITH</div><p class="bd white" style="font-size:2.8px">ipsum dolor sit amet, cons ectetuer adipiscing elit, sed diam nonummy nibh euismod tincidunt ut laoreet dolore magna aliquam erat volutpat. Ut wisi enim ad minim veniam, quis nostrud</p></div>
    <div class="center" style="width:80px"><div role="img" aria-label="Team member portrait" style="margin:0 auto;width:48px;height:48px;border-radius:50%;border:2px solid #fff;background:radial-gradient(circle at 50% 40%,#e3c1a6,#b9c4cc 70%)"></div><div style="font-size:7px;font-weight:700;margin-top:3px;color:#1f2a2a">JOHN SMITH</div><p class="bd white" style="font-size:2.8px">ipsum dolor sit amet, cons ectetuer adipiscing elit, sed diam nonummy nibh euismod tincidunt ut laoreet dolore magna aliquam erat volutpat. Ut wisi enim ad minim veniam, quis nostrud</p></div>
  </div>
  <div class="web">www.website.com</div>
</section>

<section class="slide c3 r6">
  <div class="abs teal" style="left:220px;top:0;width:100px;height:180px"></div>
  <h2 class="ttl abs" style="left:21px;top:22px;font-size:31px;line-height:1">Thank<br>You</h2>
  <div class="abs" style="left:145px;top:37px;font-size:8px;color:#444;letter-spacing:-1px">//</div>
  <div class="photo" role="img" aria-label="Black trucker cap on a workshop counter" style="left:161px;top:21px;width:138px;height:137px;background:linear-gradient(150deg,#6b6e72,#2b2d31 45%,#4d4a44 75%,#8a7f63)"></div>
  <div class="ring" style="left:147px;top:145px;width:27px;height:27px"></div>
  <div class="abs" style="left:268px;top:9px;display:flex;gap:7px">
    <span style="width:4.5px;height:4.5px;border-radius:50%;background:var(--gold)"></span><span style="width:4.5px;height:4.5px;border-radius:50%;background:var(--gold)"></span><span style="width:4.5px;height:4.5px;border-radius:50%;background:var(--gold)"></span><span style="width:4.5px;height:4.5px;border-radius:50%;background:var(--gold)"></span>
  </div>
  <div class="dots" style="left:284px;top:167px;grid-template-columns:repeat(4,1.4px)"><i style="background:#fff"></i><i style="background:#fff"></i><i style="background:#fff"></i><i style="background:#fff"></i></div>
  <div class="abs" style="left:21px;top:108px">
    <div style="font-family:'Playfair Display',serif;font-weight:900;color:var(--teal);font-size:9px">Contact US</div>
    <div style="font-size:5.8px;color:#333;line-height:1.5;margin-top:2px">
      <div><span style="display:inline-block;width:4px;height:4px;border-radius:50%;background:var(--gold);margin-right:3px"></span>111-222-333</div>
      <div><span style="display:inline-block;width:4px;height:4px;border-radius:50%;background:var(--gold);margin-right:3px"></span>info@mailaddress.com</div>
      <div><span style="display:inline-block;width:4px;height:4px;border-radius:50%;background:var(--gold);margin-right:3px"></span>Your address, your city, box 88900</div>
    </div>
  </div>
</section>

</body>
</html>
```